Natural Light/Organic/Documentary Photography Business

I like a simple, approachable, feminine, earthy/organic feel. Earth/neutral tones, nothing too loud or obnoxious. I like the watercolor look. I don't want anything too trendy or something I'll get tired of after a couple months. As far as colors, I am much more a fan of cream/taupe/blue/green...not a fan of pink or purple at all.

Target Market(s)

Weddings & Families

Industry/Entity Type

Wedding Photography

Contact Information for Business Card

website, email, phone number

Font styles to use
Other font styles liked:
• Horizontes, Gotham

Colors

Designer to choose colors to be used in the design.

Requirements
Must have
• Website: www.meliskaverholt.com
• Phone: 482.319.6047
• Email: tessa@meliskaverholt.com
Nice to have
• I like the watercolor look but its not necessary. I like simple/earthy tones. Nothing too loud or distracting. Simple & feminine without being too girly. I like an approachable/soft feel.
• Instagram: www.instagram.com/meliskaverholtphotography/
Should not have
• NO loud colors or design or pattern. I do not want a photo of a camera or lens or anything cheesy like that.

```html
<!DOCTYPE html>
<html lang="en">
<head>
<meta charset="utf-8">
<title>Meliskaverholt Photography – Business Card</title>
<link rel="stylesheet" href="https://fonts.googleapis.com/css2?family=Source+Sans+3:wght@300;400&display=swap">
<style>
  :root {
    --backdrop: #ebebeb;
    --paper: #ffffff;
    --taupe: #8e8077;
    --ink: #3f3f3f;
    --icon: #8a7b72;
  }
  * { margin: 0; padding: 0; box-sizing: border-box; }
  html, body {
    width: 1200px;
    height: 799px;
    overflow: hidden;
    background: var(--backdrop);
    font-family: "Source Sans 3", sans-serif;
  }
  .canvas {
    position: relative;
    width: 1200px;
    height: 799px;
  }
  .card {
    position: absolute;
    left: 313px;
    width: 584px;
    height: 334px;
  }
  .card--front { top: 51px; background: var(--paper); }
  .card--back  { top: 413px; background: var(--taupe); }

  .wordmark {
    position: absolute;
    left: 0;
    width: 100%;
    text-align: center;
    font-weight: 300;
    white-space: nowrap;
  }
  .card--front .wordmark {
    top: 66px;
    font-size: 24px;
    letter-spacing: 0.04em;
    color: var(--taupe);
  }
  .card--back .wordmark {
    top: 140px;
    font-size: 32px;
    letter-spacing: 0.04em;
    color: var(--paper);
  }

  .name-band {
    position: absolute;
    top: 174px;
    left: 0;
    width: 100%;
    height: 34px;
    background: var(--taupe);
    color: var(--paper);
    font-size: 20px;
    font-weight: 400;
    line-height: 34px;
    text-align: center;
  }

  .contact-list {
    position: absolute;
    top: 265px;
    list-style: none;
    font-size: 15px;
    color: var(--ink);
  }
  .contact-list--left  { left: 38px; }
  .contact-list--right { left: 330px; }
  .contact-item {
    display: flex;
    align-items: center;
    height: 19px;
    white-space: nowrap;
  }
  .contact-item svg {
    width: 13px;
    height: 13px;
    margin-right: 10px;
    flex: none;
    fill: var(--icon);
  }

  .back-url {
    position: absolute;
    top: 278px;
    left: 0;
    width: 100%;
    text-align: center;
    color: var(--paper);
    font-size: 15px;
    font-weight: 400;
    letter-spacing: 0.25em;
  }
</style>
</head>
<body>
<main class="canvas">

  <section class="card card--front" aria-label="Card front">
    <p class="wordmark">Meliskaverholt Photography</p>
    <div class="name-band">Tessa Meliskaverholt</div>

    <ul class="contact-list contact-list--left">
      <li class="contact-item">
        <svg viewBox="0 0 16 16" aria-hidden="true"><path d="M2 4c0-1 1-2 6-2s6 1 6 2v1.5h-3V4.5H5v1H2z"/><path d="M4 7h8l2 7H2z"/><circle cx="8" cy="10.5" r="1.6" fill="#fff"/></svg>
        482.319.6047
      </li>
      <li class="contact-item">
        <svg viewBox="0 0 16 16" aria-hidden="true"><path d="M1 3h14v1.2L8 9 1 4.2z"/><path d="M1 6l7 4.6L15 6v7H1z"/></svg>
        tessa@meliskaverholt.com
      </li>
    </ul>

    <ul class="contact-list contact-list--right">
      <li class="contact-item">
        <svg viewBox="0 0 16 16" aria-hidden="true"><circle cx="8" cy="8" r="7"/><path d="M4 5c2 0 2 2 4 2s1 3-1 3-1 3-2 3M10 3c0 2 2 2 3 3" stroke="#fff" stroke-width="1.2" fill="none"/></svg>
        www.meliskaverholt.com
      </li>
      <li class="contact-item">
        <svg viewBox="0 0 16 16" aria-hidden="true"><rect x="1.5" y="1.5" width="13" height="13" rx="2"/></svg>
        meliskaverholtphotography
      </li>
    </ul>
  </section>

  <section class="card card--back" aria-label="Card back">
    <p class="wordmark">Meliskaverholt Photography</p>
    <p class="back-url">WWW.MELISKAVERHOLT.COM</p>
  </section>

</main>
</body>
</html>
```